依頼詳細
チラシのデザインの原案をデータ化していただきたく、よろしくお願いします。
園児募集中の丸はそれぞれ違ったカラフルな色で目立つようにお願いします。
記載項目
添付の手書き原案を基に、添付のグーグルマップとブログQRを所定の位置に盛り込んでください。

住所:川崎区緑葉台4-27-6-203
電話:050-3192-7461
サイズ
A4
ページ数
片面
希望イメージ
シンプル 複雑
単色 カラフル
暗い 明るい
日常 高級
遊び心 厳粛
未来的 伝統的
女性的 男性的
希望する色
赤系、ピンクx白系:色については手書き案を参照ください
納品ファイル
• イラストレーター形式 (.ai)
補足説明

イメージと合っていたため、バランスが良かったため

ご対応いただきありがとうございました。

```html
<!DOCTYPE html>
<html lang="ja">
<head>
<meta charset="UTF-8">
<title>ひだまり保育園 園児募集中</title>
<link rel="stylesheet" href="https://fonts.googleapis.com/css2?family=M+PLUS+Rounded+1c:wght@400;700;800;900&display=swap">
<style>
:root{
  --pink:#ef6f8f;
  --pink-deep:#e2456e;
  --pink-soft:#fbd3dc;
  --pink-bg:#f9c7d3;
  --white:#ffffff;
  --ink:#4a3b3f;
  --red:#e23a4a;
  --c1:#f2668b;
  --c2:#5fbf6a;
  --c3:#f5b82e;
  --c4:#f28a3c;
  --c5:#4fa9dc;
  --b-blue:#cfe8f7;
  --b-green:#d6f0cf;
  --b-peach:#fde0c8;
  --b-yellow:#fff3b8;
  --b-pink:#fcdbe6;
  --b-lav:#e6dcf5;
  --map:#eef0f2;
}
*{margin:0;padding:0;box-sizing:border-box}
html,body{width:854px;height:1200px;overflow:hidden;background:var(--white)}
body{font-family:"M PLUS Rounded 1c",sans-serif;color:var(--ink);position:relative}
.flyer{position:absolute;inset:0;background:var(--white)}
.header{position:absolute;top:28px;left:0;right:0;height:80px}
.brand{position:absolute;left:190px;top:6px;display:flex;align-items:center;gap:12px}
.brand-dot{width:40px;height:40px;border-radius:50%;background:var(--pink)}
.brand-name{font-size:42px;font-weight:800;color:var(--pink-deep);letter-spacing:2px}
.badge{position:absolute;right:56px;top:0;width:96px;height:96px;border-radius:50%;background:var(--pink-soft);border:3px solid var(--pink);display:flex;align-items:center;justify-content:center;text-align:center;font-size:15px;font-weight:800;color:var(--pink-deep);line-height:1.3}
.headline{position:absolute;top:120px;left:0;right:0;display:flex;justify-content:center;gap:14px}
.headline span{width:138px;height:138px;border-radius:50%;display:flex;align-items:center;justify-content:center;font-size:84px;font-weight:900;color:var(--white);border:5px solid var(--white);box-shadow:0 0 0 3px rgba(0,0,0,.05)}
.headline span:nth-child(1){background:var(--c1)}
.headline span:nth-child(2){background:var(--c2)}
.headline span:nth-child(3){background:var(--c3)}
.headline span:nth-child(4){background:var(--c4)}
.headline span:nth-child(5){background:var(--c5)}
.features{position:absolute;top:285px;left:0;right:0;height:560px;background:linear-gradient(180deg,#fde4ea 0%,var(--pink-bg) 100%)}
.strings{position:absolute;inset:0}
.balloon{position:absolute;border-radius:50%;display:flex;flex-direction:column;align-items:center;justify-content:center;text-align:center;padding:22px}
.balloon h3{font-size:30px;font-weight:900;line-height:1.15;margin-bottom:8px}
.balloon p{font-size:13px;line-height:1.5;font-weight:700;color:var(--ink)}
.b-station{left:30px;top:30px;width:230px;height:230px;background:var(--b-blue)}
.b-station h3{color:#2f86c7}
.b-clean{left:300px;top:10px;width:200px;height:200px;background:var(--b-green)}
.b-clean h3{color:#3c9e47}
.b-age{left:560px;top:25px;width:240px;height:240px;background:var(--b-peach)}
.b-age h3{color:#e0702a}
.b-year{left:60px;top:280px;width:200px;height:200px;background:var(--b-yellow)}
.b-year h3{color:#d99800}
.b-temp{left:300px;top:255px;width:220px;height:220px;background:var(--b-pink)}
.b-temp h3{color:var(--pink-deep)}
.b-first{left:575px;top:290px;width:210px;height:210px;background:var(--b-lav)}
.b-first h3{color:#8a5cc7}
.contact{position:absolute;top:830px;left:24px;right:24px;height:310px;background:var(--white);border-radius:24px;border:3px solid var(--pink-soft)}
.contact-brand{position:absolute;left:26px;top:22px;display:flex;align-items:center;gap:10px}
.contact-brand .brand-dot{width:30px;height:30px}
.contact-brand .brand-name{font-size:30px}
.contact-badge{position:absolute;left:300px;top:22px;width:56px;height:56px;border-radius:50%;background:var(--pink-soft);border:2px solid var(--pink)}
.lead{position:absolute;left:26px;top:80px;font-size:24px;font-weight:800;color:var(--red)}
.info{position:absolute;left:26px;top:122px;font-size:13px;line-height:1.6;font-weight:700}
.phone{position:absolute;left:24px;top:170px;display:flex;align-items:center;gap:8px;font-size:40px;font-weight:900;color:var(--pink-deep);letter-spacing:1px}
.blog{position:absolute;left:26px;top:232px;font-size:13px;font-weight:700}
.map-label{position:absolute;right:30px;top:10px;font-size:16px;font-weight:800;color:var(--pink-deep)}
.map{position:absolute;right:20px;top:36px;width:400px;height:258px;background:var(--map);border-radius:10px}
.move-note{position:absolute;right:330px;top:44px;width:88px;padding:8px 6px;background:var(--pink);color:var(--white);font-size:13px;font-weight:800;text-align:center;line-height:1.4;border-radius:8px}
.footer{position:absolute;left:0;right:0;bottom:0;height:52px;background:var(--pink);color:var(--white);display:flex;align-items:center;justify-content:center;font-size:22px;font-weight:800;letter-spacing:1px}
</style>
</head>
<body>
<main class="flyer">
  <header class="header">
    <div class="brand"><span class="brand-dot"></span><span class="brand-name">ひだまり保育園</span></div>
    <div class="badge">川崎認定<br>保育園</div>
  </header>

  <h1 class="headline" aria-label="園児募集中">
    <span>園</span><span>児</span><span>募</span><span>集</span><span>中</span>
  </h1>

  <section class="features">
    <svg class="strings" width="854" height="560" viewBox="0 0 854 560">
      <g fill="none" stroke="#e79bb0" stroke-width="2">
        <path d="M145 260 Q260 420 420 545"/>
        <path d="M400 210 Q410 380 420 545"/>
        <path d="M680 265 Q560 420 420 545"/>
        <path d="M160 480 Q300 520 420 545"/>
        <path d="M410 475 L420 545"/>
        <path d="M680 500 Q540 530 420 545"/>
      </g>
    </svg>
    <div class="balloon b-station"><h3>川崎駅から<br>スグ!</h3><p>駅から徒歩圏内で<br>送り迎えもラクラク。<br>小さな園庭もあります。</p></div>
    <div class="balloon b-clean"><h3>清潔</h3><p>新しい園舎で<br>園内もきれいで<br>清潔です。</p></div>
    <div class="balloon b-age"><h3>生後5ヵ月〜</h3><p>生後5ヵ月から<br>入園可能です。<br>年齢はご相談下さい。</p></div>
    <div class="balloon b-year"><h3>1年中<br>入園OK!</h3><p>年度途中でも<br>入園できます。</p></div>
    <div class="balloon b-temp"><h3>一時保育</h3><p>親御さんのリフレッシュや<br>急な用事の際にも<br>ご利用いただけます。</p></div>
    <div class="balloon b-first"><h3>先着順</h3><p>少人数の保育園です。<br>定員になり次第<br>受付終了となります。</p></div>
  </section>

  <section class="contact">
    <div class="contact-brand"><span class="brand-dot"></span><span class="brand-name">ひだまり保育園</span></div>
    <div class="contact-badge"></div>
    <p class="lead">お気軽にお問い合わせ下さい!</p>
    <p class="info">住所 〒210-0999 川崎区緑葉台4-27-6-203<br>見学は随時受付中です</p>
    <p class="phone">
      <svg width="34" height="34" viewBox="0 0 24 24" aria-hidden="true"><path fill="#e2456e" d="M6.6 10.8a15.1 15.1 0 0 0 6.6 6.6l2.2-2.2a1 1 0 0 1 1-.25 11.4 11.4 0 0 0 3.6.57 1 1 0 0 1 1 1V20a1 1 0 0 1-1 1A17 17 0 0 1 3 4a1 1 0 0 1 1-1h3.5a1 1 0 0 1 1 1c0 1.25.2 2.45.57 3.57a1 1 0 0 1-.25 1z"/></svg>
      050-3192-7461
    </p>
    <p class="blog">BLOG https://example-blog.jp/hidamarihoikuen</p>
    <p class="map-label">アクセスマップ</p>
    <div class="map" role="img" aria-label="川崎駅から保育園までの道順を示す地図"></div>
    <p class="move-note">2018年<br>7月頃<br>引越し予定</p>
  </section>

  <footer class="footer">一緒に働いてくれる保育士さんも募集中です!</footer>
</main>
</body>
</html>
```